Roll-Up Banner für Glückswebsite
Das war eine großartige Zusammenarbeit und unserem sehr knappen Zeitplan extrem entgegenkommend. Das design ist gleichzeitig seriös und trotzdem jung und dynamisch! Perfekt!
Zielgruppe
Die Website, www.freudenpfad.de ermöglicht es jedem Interessierten kostenlos mehr über das eigene Lebensglück, persönliche Stärken, und die eigene Lebenszufriedenheit herauszufinden. Interessierte können online Fragebögen ausfüllen, und erhalten neben einer detaillierten Rückmeldung über die eigenen Möglichkeiten und Stärken, Hinweise dazu, wie Sie an Ihrem eigenen Potenzial arbeiten können. Es handelt sich um ein Kooperationsprojekt der Nordischen Vereinigung für Heitere Seelenkunde der Uni Wendelstein, der HK-Lindau, der Health Academy Marbach und der Uni Falkenried. Zielgruppe für das Banner sind Menschen, die selbst mit Klienten im Kontext der Positiven Psychologie arbeiten oder Menschen, die sich Ihrem eigenen Lebensglück zuwenden wollen.
Aufgabenstellung
Es handelt sich um ein Roll-up Banner in den Maßen 1m Breite und 2 Meter Höhe.
Das Banner sollte so angelegt sein, dass es interessierten Besuchern auf Kongressen vermittelt, was es mit der Seite Freudenpfad.de auf sich hat. Also wissenschaftlich evaluierte kostenfreie online-Fragebögen, die Menschen dabei helfen Ihre eigenen Stärken und Potenziale zu entdecken und dem eigenen Glück näher zu kommen.
Es sollte außerdem das Logo der NVHS darauf zu sehen sein, sowie kleiner die Logos der Forschungskooperationspartner, HK-Lindau, Uni Wendelstein, Uni Falkenried, Health Academy Marbach.
Die Farben sollten zum Logo der NVHS passen.

```html
<!DOCTYPE html>
<html lang="de">
<head>
<meta charset="utf-8">
<title>NVHS Roll-Up – Freudenpfad.de</title>
<link rel="stylesheet" href="https://fonts.googleapis.com/css2?family=Fira+Sans:wght@300;400;500&display=swap">
<style>
  :root {
    --navy: #1d3a6b;
    --navy-deep: #0f2a5c;
    --teal: #2aa7c0;
    --teal-soft: #52b3b0;
    --green: #5ea848;
    --paper: #f5f5f7;
    --stage: #c3c9d4;
    --white: #ffffff;
    --dot-1: #74c0d4;
    --dot-2: #22968e;
    --dot-3: #2c9560;
    --dot-4: #1f3a6e;
  }
  * { margin: 0; padding: 0; box-sizing: border-box; }
  html, body { width: 768px; height: 1200px; overflow: hidden; }
  body { background: var(--stage); font-family: "Fira Sans", sans-serif; color: var(--navy); position: relative; }

  .banner { position: absolute; left: 84px; top: 10px; width: 600px; height: 1180px; background: var(--paper); overflow: hidden; }

  .brand { position: absolute; left: 48px; top: 70px; display: flex; align-items: center; gap: 10px; }
  .brand-dot { width: 22px; height: 22px; border-radius: 50%; background: var(--teal); }
  .brand-name { font-size: 24px; font-weight: 500; letter-spacing: 2px; color: var(--navy); }
  .brand-sub { position: absolute; left: 80px; top: 120px; font-size: 9px; line-height: 11px; font-weight: 500; color: var(--navy); width: 130px; }

  .url-band { position: absolute; left: 0; top: 167px; width: 600px; height: 49px;
    background: linear-gradient(90deg, var(--teal-soft), var(--teal));
    display: flex; align-items: center; justify-content: center; }
  .url-band span { font-size: 34px; font-weight: 400; color: var(--navy); }

  .hero-photo { position: absolute; left: 37px; top: 216px; width: 200px; height: 228px;
    background: radial-gradient(ellipse at 50% 45%, #e9c49a 0%, #d6a46e 45%, #f0e6da 85%, var(--paper) 100%); }
  .hero-question { position: absolute; left: 242px; top: 302px; width: 340px; font-size: 26.5px; font-weight: 400; line-height: 35px; color: var(--navy); }

  .info-panel { position: absolute; left: 0; top: 444px; width: 600px; height: 587px;
    background: linear-gradient(160deg, #5eae9c 0%, #3aa2a8 35%, #47a07a 65%, var(--green) 100%); }
  .info-rule { position: absolute; left: 0; top: 1031px; width: 600px; height: 6px; background: var(--navy-deep); }

  .intro { position: absolute; left: 53px; top: 496px; width: 490px; font-size: 17px; line-height: 22.5px; font-weight: 400; color: var(--navy); }

  .steps-line { position: absolute; left: 68px; top: 640px; width: 2px; height: 230px; background: var(--white); }
  .step-dot { position: absolute; left: 55px; width: 28px; height: 28px; border-radius: 50%; border: 2px solid var(--white); }
  .step-title { position: absolute; left: 102px; font-size: 23px; font-weight: 400; color: var(--navy); white-space: nowrap; }
  .step-note { position: absolute; left: 102px; font-size: 17px; font-weight: 400; color: var(--navy); white-space: nowrap; }

  .badge { position: absolute; left: 416px; top: 704px; width: 190px; height: 50px; background: var(--navy-deep);
    transform: rotate(-3deg); transform-origin: left center; color: var(--white);
    font-size: 12.5px; line-height: 17px; text-align: center; padding: 8px 10px 0 0; white-space: nowrap; }

  .partners-title { position: absolute; left: 53px; top: 1060px; font-size: 17.5px; font-weight: 400; color: var(--navy); }
  .partners { position: absolute; left: 53px; top: 1108px; width: 500px; display: flex; justify-content: space-between; align-items: center; }
  .partner { display: flex; align-items: center; gap: 6px; font-size: 11px; font-weight: 400; color: var(--navy); }
  .partner-mark { width: 18px; height: 18px; border-radius: 50%; background: #8a95a8; }
</style>
</head>
<body>
  <main class="banner">
    <div class="brand"><span class="brand-dot"></span><span class="brand-name">NVHS</span></div>
    <p class="brand-sub">Nordische Vereinigung für Heitere Seelenkunde</p>

    <div class="url-band"><span>www.freudenpfad.de</span></div>

    <div class="hero-photo" role="img" aria-label="Foto einer lächelnden jungen Frau mit blondem Haar"></div>
    <h1 class="hero-question">Wollen Sie mehr über sich und Ihre Stärken erfahren?</h1>

    <section class="info-panel"></section>
    <div class="info-rule"></div>

    <p class="intro">Unter www.freudenpfad.de haben Sie die Möglichkeit kostenfrei die neusten wissenschaftlichen Fragebögen im Bereich der Positiven Psychologie zu nutzen und ein detailliertes Feedback zu Ihren Ergebnissen zu erhalten.</p>

    <div class="steps-line"></div>
    <span class="step-dot" style="top:621px;background:var(--dot-1)"></span>
    <span class="step-dot" style="top:708px;background:var(--dot-2)"></span>
    <span class="step-dot" style="top:797px;background:var(--dot-3)"></span>
    <span class="step-dot" style="top:855px;background:var(--dot-4)"></span>

    <h2 class="step-title" style="top:619px">Persönliches Konto einrichten</h2>
    <p class="step-note" style="top:655px">– und damit immer Zugriff auf Ihre Ergebnisse haben</p>
    <h2 class="step-title" style="top:706px">Online-Fragebogen ausfüllen</h2>
    <p class="step-note" style="top:743px">unter www.freudenpfad.de</p>
    <h2 class="step-title" style="top:795px">Persönliche Rückmeldung erhalten</h2>
    <h2 class="step-title" style="top:853px">Ein noch erfüllteres Leben gestalten</h2>
    <p class="step-note" style="top:880px">– mit unseren Hinweisen</p>

    <div class="badge">wissenschaftlich evaluiert<br>kostenfrei | anonym</div>

    <h3 class="partners-title">Forschungskooperationspartner</h3>
    <div class="partners">
      <span class="partner"><span class="partner-mark"></span>Uni Wendelstein</span>
      <span class="partner">Health Academy Marbach</span>
      <span class="partner"><span class="partner-mark"></span>HK-Lindau</span>
      <span class="partner"><span class="partner-mark"></span>Uni Falkenried</span>
    </div>
  </main>
</body>
</html>
```